Brochure Design Project

This will be a tri-fold full 8.5x11 brochure that will be distributed and sitting in Oncology offices all throughout the US. It is a lead generation and referral designed piece that it to target all patients, Cancer primarily, but all critically ill patients and seniors above the age of 70. We want our service to go beyond just a financial transaction, we want to educate patients of their rights within a life insurance policy and if we cannot help them personally, do want to assist them by referring them to other agencies and non profits than can. ( I want to redesign the brochure attached, it can be very similar and need only minor changes to content, but would welcome all suggestions on improving message, and in gaining attention, picture substitutions and change of colors, along with the layout itself can be improved upon, and I need this piece to look very professional and appropriate for medical offices. I will be needing assistance on several upcoming projects and will also have great printing demands.

Target Market(s)

Cancer patients
all chronically and critically ill patients
all seniors above age 70

Industry/Entity Type

Life Insurance

Requirements
Must have
• Cancer and the terminally ill
Nice to have
• seniors above 70

```html
<!DOCTYPE html>
<html lang="en">
<head>
<meta charset="utf-8">
<title>Beacon Settlements Brochure</title>
<link href="https://fonts.googleapis.com/css2?family=Arimo:wght@400;700&family=PT+Sans:wght@400;700&display=swap" rel="stylesheet">
<style>
:root{
  --blue:#4a78c2;
  --blue-dark:#2f5aa8;
  --blue-soft:#8fa9da;
  --orange:#f7a823;
  --pink:#f7c3d6;
  --pink-text:#f6b9d3;
  --ink:#222;
  --white:#fff;
  --page:#e9e6e2;
}
*{margin:0;padding:0;box-sizing:border-box}
html,body{width:801px;height:1200px;overflow:hidden;background:var(--page)}
.stage{position:relative;width:1001px;height:1500px;transform:scale(.8);transform-origin:0 0;font-family:"Arimo",Arial,sans-serif}
.sheet{position:absolute;left:40px;width:922px;height:712px;background:var(--white);box-shadow:0 3px 10px rgba(0,0,0,.25);overflow:hidden}
.sheet-outside{top:24px}
.sheet-inside{top:762px}
.panel{position:absolute;top:0;width:308px;height:100%;overflow:hidden}
.p1{left:0}.p2{left:307px}.p3{left:615px;width:307px}
.blue{background:var(--blue);color:var(--white)}
.abs{position:absolute}
.photo{position:absolute;left:0;width:100%}
.curve{position:absolute;left:0;width:100%}

/* outside left */
.benefits-title{left:22px;top:24px;font-size:22px;font-weight:700;color:var(--orange)}
.benefits{left:22px;top:56px;list-style:none;font-size:14px;line-height:17.5px;color:var(--white)}
.benefits li{padding-left:12px;position:relative}
.benefits li::before{content:"";position:absolute;left:0;top:6px;width:6px;height:6px;border:1px solid var(--white);border-radius:50%}
.gift{left:22px;top:630px;font-size:22px;font-weight:700;line-height:33px;color:var(--pink-text)}

/* brand name */
.brand{font-family:"Arimo",Arial,sans-serif;font-weight:700;color:var(--blue-dark);text-align:center;letter-spacing:2px}

/* mail panel */
.mail-top{left:0;top:0;width:100%;height:260px;background:var(--white)}
.mail-pink{left:0;top:0;width:100%;height:100%;background:var(--pink)}
.return-note{left:0;width:100%;top:128px;text-align:center;font-size:13px;color:var(--ink);line-height:18px}
.phone-big{left:0;width:100%;text-align:center;font-size:38px;font-weight:700;color:var(--ink);letter-spacing:-.5px}
.confidential{left:0;width:100%;top:205px;text-align:center;font-size:11px;line-height:11px;color:var(--ink)}
.reply{position:absolute;left:308px;top:266px;width:470px;height:308px;transform-origin:0 0;transform:rotate(90deg);color:var(--ink)}
.reply-box{left:40px;top:14px;width:275px;border:1.5px solid var(--ink);padding:2px 6px}
.reply-box b{display:block;font-size:20px;letter-spacing:.5px}
.reply-box span{font-size:11px;display:flex;justify-content:space-between}
.reply-pay{left:40px;top:72px;font-size:8.5px;letter-spacing:.3px}
.reply-to{left:40px;top:90px;font-size:16px;font-weight:700}
.reply-addr{left:40px;top:112px;font-size:15px;line-height:20px}
.no-postage{left:350px;top:30px;width:100px;height:86px;border:1px solid var(--ink);font-size:10px;line-height:12px;text-align:center;padding-top:10px;color:var(--blue-dark)}

/* outside right */
.help-title{left:0;width:100%;top:8px;text-align:center;font-size:34px;font-weight:700;color:var(--orange)}
.help-text{left:10px;width:287px;top:47px;text-align:center;font-size:15px;font-weight:700;line-height:24px;color:var(--pink-text)}

/* inside */
.money-title{left:20px;top:362px;font-size:28px;font-weight:700;color:var(--pink-text)}
.money-copy{left:20px;top:402px;width:266px;font-family:"PT Sans",Arial,sans-serif;font-size:13.5px;line-height:17px;color:var(--white);text-align:justify}
.money-copy p{margin-bottom:16px}
.money-close{left:20px;top:638px;font-size:14px;font-weight:700;line-height:21px;color:var(--orange)}
.intro{left:20px;top:28px;width:270px;font-family:"PT Sans",Arial,sans-serif;font-size:12px;line-height:19.5px;color:var(--ink);text-align:justify}
.intro strong{color:var(--orange);font-size:16px;font-weight:700}
.intro p{margin-bottom:12px}
.tagline{left:16px;top:228px;font-size:14px;font-weight:700;color:var(--blue);line-height:22px}
.tagline .big{font-size:21px}
.quotes{left:10px;top:22px;width:290px;font-family:"PT Sans",Arial,sans-serif;font-size:14px;line-height:18px;color:var(--pink-text)}
.quotes p{margin-bottom:16px;padding-left:14px;position:relative}
.quotes p::before{content:"\201C";position:absolute;left:0;top:-4px;font-size:24px;font-weight:700;color:var(--white)}
.eligible{left:24px;top:160px;width:270px;color:var(--white)}
.eligible .kicker{font-size:13px;font-weight:700;color:var(--orange)}
.eligible .headline{font-size:23px;font-weight:700;color:var(--orange);line-height:26px}
.eligible .call{font-size:12px;font-weight:700;margin-top:6px}
.eligible .details{font-family:"PT Sans",Arial,sans-serif;font-size:11px;line-height:18px}
.eligible .phone{font-size:36px;font-weight:700;color:var(--orange);line-height:40px}
.form-area{left:0;top:324px;width:100%;height:390px;background:var(--white)}
.form{position:absolute;left:0;top:390px;width:390px;height:307px;transform-origin:0 0;transform:rotate(-90deg);color:var(--ink)}
.form-title{left:20px;top:12px;font-size:16px;letter-spacing:.3px}
.field{position:absolute;left:20px;width:352px;height:20px;display:flex;align-items:flex-end;font-size:10px;font-weight:700;gap:4px}
.field i{flex:1;border-bottom:1px solid var(--ink);height:1px}
.field small{font-size:9px;font-weight:700}
.form-note{left:20px;top:276px;font-size:10px;font-family:"PT Sans",Arial,sans-serif}
</style>
</head>
<body>
<div class="stage">

  <!-- Outside sheet -->
  <section class="sheet sheet-outside">
    <div class="panel p1 blue">
      <h2 class="abs benefits-title">BEACON SETTLEMENTS</h2>
      <ul class="abs benefits">
        <li>Reduce  financial Stress</li>
        <li>Pay for Uninsured Healthcare Cost</li>
        <li>Pay for Alternative Treatment</li>
        <li>Improve Quality of Life</li>
        <li>pay off Debt</li>
        <li>Take a Long Awaited vacation or<br>Dream Trip</li>
        <li>Make Cash Gifts to family and Friends</li>
        <li>Fulfill Life Wishes</li>
        <li>Pay for College Funding</li>
        <li>Make Home Improvements</li>
        <li>Donate to Church or Charity</li>
        <li>See the Money Enjoyed by<br>Relatives Now</li>
        <li>Invest in Financial Vehicles</li>
        <li>Buy a New car</li>
        <li>Fund Long Term Care Expenses</li>
        <li>Plan Ahend for Final Estate Needs</li>
      </ul>
      <div class="photo" style="top:378px;height:235px;background:linear-gradient(135deg,#c8cdd4,#eef0f2 55%,#9aa3ad)" role="img" aria-label="Patient resting in a hospital bed, smiling"></div>
      <svg class="curve" style="top:372px" width="308" height="40" viewBox="0 0 308 40"><path d="M0 0H308V12Q180 -4 0 30Z" fill="var(--blue)"/><path d="M0 24Q170 -4 308 14" stroke="var(--orange)" stroke-width="4" fill="none"/></svg>
      <svg class="curve" style="top:590px" width="308" height="30" viewBox="0 0 308 30"><path d="M0 30V10Q150 28 308 4V30Z" fill="var(--blue)"/></svg>
      <p class="abs gift">HOPE IS OUR DESIRED<br>GIFT TO YOU!</p>
    </div>

    <div class="panel p2">
      <div class="abs mail-pink"></div>
      <div class="abs mail-top"></div>
      <svg class="curve" style="top:196px" width="308" height="80" viewBox="0 0 308 80"><path d="M0 0Q150 40 308 0V40Q150 80 0 40Z" fill="var(--blue)"/><path d="M0 24Q150 64 308 24" stroke="var(--white)" stroke-width="3" fill="none" opacity=".0"/></svg>
      <div class="abs brand" style="left:0;width:100%;top:60px;font-size:30px;letter-spacing:4px">BEACON</div>
      <div class="abs brand" style="left:0;width:100%;top:96px;font-size:14px;font-weight:400;letter-spacing:6px">Settlements</div>
      <p class="abs return-note">Please return the attached postcard or<br>Call Toll Free</p>
      <p class="abs phone-big" style="top:160px">800-555-0199</p>
      <p class="abs confidential">All Communication will<br>be kept strictly confidential!</p>
      <div class="reply">
        <div class="abs reply-box"><b>BUSINESS REPLY MAIL</b><span><em style="font-style:normal">First-Class Mail&nbsp;&nbsp; Permit No. 2417</em><em style="font-style:normal">GEORGIA</em></span></div>
        <p class="abs reply-pay">POSTAGE WILL BE PAID BY ADDRESSEE</p>
        <p class="abs reply-to">BEACON SETTLEMENTS</p>
        <p class="abs reply-addr">480 Maple Crest Dr. Riverton,<br>Georgia 30099</p>
        <p class="abs no-postage">NO POSTAGE<br>NECESSARY<br>IF MAILED<br>IN THE<br>UNITED STATES</p>
      </div>
    </div>

    <div class="panel p3">
      <div class="abs blue" style="left:0;top:0;width:100%;height:230px"></div>
      <h2 class="abs help-title">WE CAN HELP</h2>
      <p class="abs help-text">Provide the information and guidance you need to maximize insurance benefits and learn about the various<br>FINANCIAL RESOURCES AVAILABLE</p>
      <div class="photo" style="top:212px;height:290px;background:linear-gradient(160deg,#a7a49e,#d9d2c8 50%,#8f8a83)" role="img" aria-label="Woman in treatment looking ahead with quiet hope"></div>
      <svg class="curve" style="top:176px" width="307" height="70" viewBox="0 0 307 70"><path d="M0 0H307V24Q150 20 0 60Z" fill="var(--blue)"/><path d="M120 20Q220 2 307 30" stroke="var(--orange)" stroke-width="7" fill="none"/><path d="M0 62Q150 24 307 36" stroke="var(--blue-soft)" stroke-width="5" fill="none"/></svg>
      <svg class="curve" style="top:462px" width="307" height="60" viewBox="0 0 307 60"><path d="M0 60V22Q150 60 307 10V60Z" fill="var(--white)"/><path d="M0 22Q150 60 307 10" stroke="var(--blue-soft)" stroke-width="5" fill="none"/></svg>
      <div class="abs brand" style="left:0;width:100%;top:575px;font-size:30px;letter-spacing:4px">BEACON</div>
      <div class="abs brand" style="left:0;width:100%;top:612px;font-size:14px;font-weight:400;letter-spacing:6px">Settlements</div>
      <p class="abs phone-big" style="top:646px">800-555-0199</p>
    </div>
  </section>

  <!-- Inside sheet -->
  <section class="sheet sheet-inside">
    <div class="panel p1 blue">
      <div class="photo" style="top:14px;height:320px;background:linear-gradient(135deg,#5b5a58,#b9b4ab 50%,#4b4440)" role="img" aria-label="Family gathered at a loved one's hospital bedside"></div>
      <svg class="curve" style="top:0" width="308" height="60" viewBox="0 0 308 60"><path d="M0 0H308V6Q160 20 0 48Z" fill="var(--blue)"/><path d="M150 22Q240 4 308 4" stroke="var(--orange)" stroke-width="7" fill="none"/><path d="M0 52Q130 22 300 14" stroke="var(--blue-soft)" stroke-width="5" fill="none"/></svg>
      <svg class="curve" style="top:300px" width="308" height="40" viewBox="0 0 308 40"><path d="M0 40V8Q160 34 308 6V40Z" fill="var(--blue)"/><path d="M0 8Q160 34 308 6" stroke="var(--blue-soft)" stroke-width="5" fill="none"/></svg>
      <h2 class="abs money-title">IT'S YOUR MONEY</h2>
      <div class="abs money-copy">
        <p>Why do insurance companies conceal the fact that policy holders may be entitled to additional cash benefits?</p>
        <p>Why are bankruptcy rates among cancer patients and seniors more than double than that of the general population?</p>
        <p>Why do patients who are receiving care feel unsure about discussing the subject of MONEY and the effects it can have both emotionally and physically?</p>
      </div>
      <p class="abs money-close">HEALING &amp; RECOVERY should be the<br>primary concern for all patients<br><span style="font-size:16px">“NOT MONEY” or “THE LACK OF”</span></p>
    </div>

    <div class="panel p2">
      <div class="abs intro">
        <p><strong>Everyone</strong> on the journey of medical recovery should have access to FINANCIAL SUPPORT that improves quality of life and provides relief from distress.</p>
        <p><strong>We Can Help</strong> provide the information and guidance you need to learn more about your FINANCIAL RESOURCES AVAILABLE</p>
      </div>
      <p class="abs tagline">TURNING &nbsp;<span class="big">“BEACON”</span> INTO REALITY<br><span style="font-size:15.5px">WWW.BEACONSETTLEMENTS.COM</span></p>
      <div class="photo" style="top:325px;height:387px;background:linear-gradient(150deg,#c9b79a,#eee7dc 50%,#a99a86)" role="img" aria-label="Smiling doctor, nurse and senior patient standing together"></div>
      <svg class="curve" style="top:310px" width="308" height="50" viewBox="0 0 308 50"><path d="M0 0H308V50Q160 0 0 28Z" fill="var(--white)"/><path d="M0 28Q170 -6 308 40" stroke="var(--orange)" stroke-width="9" fill="none"/></svg>
    </div>

    <div class="panel p3">
      <div class="abs blue" style="left:0;top:0;width:100%;height:324px"></div>
      <div class="abs quotes">
        <p>If You Have Been Diagnosed With A Life Threatening Illness &amp; Own Life Insurance Or Covered By A Group Policy! ”</p>
        <p>Were Born Before 1943 And Own Life Insurance Or Covered By A Group Policy?”</p>
      </div>
      <div class="abs eligible">
        <p class="kicker">YOU MAY BE ELIGIBLE TO RECEIVE A</p>
        <p class="headline">BEACON SETTLEMENT</p>
        <p class="call">CALL TODAY TO RECEIVE YOUR</p>
        <p class="details">FREE &amp; CONFIDENTIAL BEACON SETTLEMENT KIT<br>OR ASK ONE OF OUR FAMILY SERVICE COUNSELORS<br>FOR ASSISTANCE &nbsp;OR ADVISE ON WHERE TO TURN</p>
        <p class="phone">800-555-0199</p>
      </div>
      <div class="abs form-area">
        <div class="form">
          <p class="abs form-title">Please send me a FREE INFORMATION KIT.</p>
          <div class="field" style="top:48px">Name:<i></i></div>
          <div class="field" style="top:84px">Address:<i></i></div>
          <div class="field" style="top:122px">City:<i></i></div>
          <div class="field" style="top:158px">E - mail address:<i></i></div>
          <div class="field" style="top:194px">Phone:<i></i><small>Best time to call:</small><i></i><small>AM</small><i></i><small>PM</small></div>
          <div class="field" style="top:230px">Insurance Co:<i></i></div>
          <p class="abs form-note">All communication will be kept strictly confidential!</p>
        </div>
      </div>
    </div>
  </section>

</div>
</body>
</html>
```